A4 Childcare Spring Special Flyer

Crestwell Learning is a registered training organisation (RTO) Toid No. 47318, based in Blackburn, Victoria. We are a market leader in Professional development courses both accredited and non accredited, in order for you to maintain currency in your profession.

We need a flyer for a childcare specific spring special. The special is to offer a $50 VOLM gift card and 50% of your second training session. Conditions apply*

The training sessions available are the NEW childcare specific course: HLTAID004 Provide an emergency first aid response in an education and care setting and HLTAID003 Provide First Aid, HLTAID001 Provide Cardiopulmonary Resuscitation (CPR), 22024VIC Course in emergency management of asthma in the workplace
and 22099VIC Course in First Aid Management of Anaphylaxis.
We provide a flexible, cost effective and reliable service.
We have training locations available in Blackburn, Preston, Narre Warren and Mornington and can also provide onsite training.

We can also provide education and PRIVOS regulation consultation to the childcare provider.

Must use company logo, include phone number: (03) 5127 6481, website: www.crestwelllearning.com.au, email: marapenn@crestwelllearning.com.au

(Note that a letter with more detail will be attached with this flyer, therefore, with that in mind; use that information as desired).

The final product should be as childcare like as possible whilst also keeping our company colors (same as logo). We would also like for this flyer to stand out and be appealing to the recipient as this flyer is to gain potential clients, with emphasis on the HLTAID004 Course
Updates

Just need to update the qualifications: In the design brief I mentioned that the course; HLTAID001 Provide CPR and Asthma & Anaphyalxis.. Can this please be changed to HLTAID001 Provide Cardiopulmonary Resuscitation (CPR) And 22024VIC Course in emergency management of asthma in the workplace And 22099VIC Course in First Aid Management of Anaphylaxis (They are all singular courses) Apoligies!

Target Market(s)

Childcare centres, Out of school hours providers, pre-schools

Industry/Entity Type

Childcare

Font styles to use
Decorative

Colors
ffcf3e
f37123
faa54b

Requirements
Must have
• Company Logo
phone number
website
email
Registered Training Organisation
TOID: 47318

```html
<!DOCTYPE html>
<html lang="en">
<head>
<meta charset="utf-8">
<title>Crestwell Learning – Spring Special Flyer</title>
<link href="https://fonts.googleapis.com/css2?family=Bowlby+One+SC&family=Open+Sans:wght@400;600;700;800&display=swap" rel="stylesheet">
<style>
  :root{
    --sun:#ffcf3e;
    --tangerine:#f37123;
    --apricot:#faa54b;
    --ember:#e85a1c;
    --paper:#ffffff;
    --ink:#1d1d1d;
    --stage:#e4e4e4;
  }
  *{box-sizing:border-box;margin:0;padding:0}
  html,body{width:1200px;height:1000px;overflow:hidden}
  body{background:var(--stage);font-family:"Open Sans",Arial,sans-serif;position:relative}

  .flyer{position:absolute;left:50px;top:111px;width:1100px;height:778px;background:var(--paper);
    box-shadow:0 10px 30px rgba(0,0,0,.18)}
  .flyer__field{position:absolute;left:14px;top:14px;right:14px;bottom:14px;overflow:hidden;
    background:radial-gradient(circle at 60% 30%,var(--sun) 0%,var(--apricot) 35%,var(--tangerine) 75%)}

  .headline{position:absolute;left:0;right:0;top:14px;text-align:center;white-space:nowrap;
    font-family:"Bowlby One SC",Impact,sans-serif;font-size:76px;letter-spacing:6px;line-height:1;
    color:var(--paper);-webkit-text-stroke:2px var(--ember);
    text-shadow:3px 4px 0 #b8420f,5px 7px 9px rgba(0,0,0,.35)}
  .headline-rule{position:absolute;left:330px;right:20px;top:114px;height:2px;background:var(--paper)}

  .intro{position:absolute;left:34px;top:126px;width:540px;color:var(--paper);font-size:11.5px;font-weight:600;line-height:1.45}

  .courses{position:absolute;left:0;top:186px;width:546px;height:226px;background:var(--paper);padding:14px 20px}
  .courses__lead{font-weight:800;font-size:19px;line-height:1.15;color:var(--ink)}
  .courses__list{list-style:none;margin-top:12px;font-size:12.5px;color:var(--tangerine);line-height:1.4}
  .courses__list li{display:flex;gap:10px}
  .courses__code{font-weight:700;min-width:74px}

  .consult{position:absolute;left:34px;top:436px;width:470px;color:var(--paper);font-size:12px;line-height:1.4}
  .contact{position:absolute;left:34px;top:490px;color:var(--paper)}
  .contact__small{font-size:13px}
  .contact__title{font-weight:800;font-size:24px;line-height:1.05}
  .phone{position:absolute;left:34px;top:556px;display:flex;align-items:center;gap:8px;
    border:2px solid var(--paper);border-radius:22px;padding:4px 16px 4px 6px;color:var(--paper);font-weight:800;font-size:22px}
  .phone svg{width:28px;height:28px}

  .footer-band{position:absolute;left:0;top:620px;width:700px;height:130px;background:var(--ember);
    clip-path:polygon(0 0,100% 0,100% 70%,92% 100%,0 100%)}
  .website{position:absolute;left:34px;top:636px;color:var(--paper);font-size:22px;letter-spacing:4px}
  .email{position:absolute;left:240px;top:690px;display:flex;align-items:center;gap:10px;color:var(--paper);font-size:20px}
  .email svg{width:28px;height:20px}

  .photo{position:absolute;left:560px;top:300px;width:512px;height:280px;
    background:linear-gradient(160deg,#f26a45 0%,#ec4f3a 55%,#d9472f 100%)}
  .offer{position:absolute;left:570px;top:236px;width:500px;color:var(--paper);text-shadow:1px 2px 3px rgba(0,0,0,.3)}
  .offer__amount{font-weight:800;font-size:46px;line-height:1;display:flex;align-items:baseline;gap:14px}
  .offer__brand{font-size:30px;font-weight:800}
  .offer__card{font-size:38px;font-weight:400;margin-left:4px}
  .offer__line{font-size:21px;font-weight:600;margin-top:6px}
  .conditions{position:absolute;left:960px;top:552px;font-size:12px;color:var(--paper)}

  .brand-block{position:absolute;right:0;bottom:0;width:352px;height:170px;background:var(--paper);
    display:flex;flex-direction:column;align-items:center;justify-content:center;gap:10px}
  .brand-block__dot{width:26px;height:26px;border-radius:50%;background:var(--tangerine)}
  .brand-block__name{font-family:"Open Sans",Arial,sans-serif;font-weight:700;font-size:34px;line-height:1;color:var(--tangerine);text-align:center}
</style>
</head>
<body>
<main class="flyer">
  <div class="flyer__field">
    <h1 class="headline">SPRING SPECIAL</h1>
    <div class="headline-rule"></div>

    <p class="intro">We provide a flexible, cost effective and reliable service.<br>
      We have training locations available in Blackburn, Preston, Narre Warren<br>
      and Mornington and can also provide onsite training.</p>

    <section class="courses">
      <p class="courses__lead">The training sessions available are the<br>NEW childcare specific course</p>
      <ul class="courses__list">
        <li><span class="courses__code">HLTAID004</span><span>Provide an emergency first aid response in an education and care setting.</span></li>
        <li><span class="courses__code">HLTAID003</span><span>Provide First Aid.</span></li>
        <li><span class="courses__code">HLTAID001</span><span>Provide Cardiopulmonary Resuscitation (CPR).</span></li>
        <li><span class="courses__code">22024VIC</span><span>Course in emergency management of asthma in the workplace.</span></li>
        <li><span class="courses__code">22099VIC</span><span>Course in First Aid Management of Anaphylaxis.</span></li>
      </ul>
    </section>

    <p class="consult">We can also provide education and PRIVOS regulation consultation to the childcare provider.</p>
    <div class="contact">
      <p class="contact__small">For more informations</p>
      <p class="contact__title">CONTACT US</p>
    </div>

    <div class="footer-band"></div>
    <div class="phone">
      <svg viewBox="0 0 28 28" aria-hidden="true"><circle cx="14" cy="14" r="13" fill="none" stroke="#fff" stroke-width="2"/><path d="M10 7c1 0 2 3 2 4s-2 1-1 3 2 3 3 3 1-2 2-1 3 2 3 3-2 3-4 2-5-3-6-6-1-8 1-8z" fill="#fff"/></svg>
      <span>(03) 5127 6481</span>
    </div>
    <p class="website">www.crestwelllearning.com.au</p>
    <p class="email">
      <svg viewBox="0 0 28 20" aria-hidden="true"><rect x="1" y="1" width="26" height="18" fill="none" stroke="#fff" stroke-width="2"/><path d="M1 1l13 10L27 1" fill="none" stroke="#fff" stroke-width="2"/></svg>
      <span>marapenn@crestwelllearning.com.au</span>
    </p>

    <div class="photo" role="img" aria-label="Photo of happy preschool children cheering with raised arms in a colourful playroom"></div>
    <div class="offer">
      <p class="offer__amount">$50 <span class="offer__brand">VOLM</span><span class="offer__card">Gift Card</span></p>
      <p class="offer__line">and 50% of your second training session.*</p>
    </div>
    <p class="conditions">* Conditions apply</p>

    <div class="brand-block">
      <span class="brand-block__dot"></span>
      <p class="brand-block__name">crestwell<br>learning</p>
    </div>
  </div>
</main>
</body>
</html>
```